Contemporary Elegant Business Card Design for an International Trade Company in the Wine Industry

We need a new business card design for an international trade company in the wine and winemaking industry. The overall feel of the card should be contemporary, upscale, luxurious and elegant. It should communicate confidence and professionalism. The colors should complementary to our logo design (burgundy, gold, and black).
Inspiration: rich velvet tapestry
The card should include the following information:
Business: Brovenna Trading/Shipping, LLC.
Name: Marcus T. Hollenbrand
Title: CEO
Email: mark@brovennatrading.example
Phone: 555-294-6172
www.brovennatrading.example
Updates
Project Deadline Extended
Reason: We'd like the designers that we requested some additional designs from to still submit designs. Thank you!
Industry/Entity Type
Business
Contact Information for Business Card
Title: CEO
Phone: 555-294-6172
www.brovennatrading.example
Look and feel

```html
<!DOCTYPE html>
<html lang="en">
<head>
<meta charset="utf-8">
<title>Brovenna Trading/Shipping – Business Card</title>
<link rel="stylesheet" href="https://fonts.googleapis.com/css2?family=Lato:wght@400;700&display=swap">
<style>
  :root {
    --stage-top: #262626;
    --stage-bottom: #050505;
    --paper: #ffffff;
    --burgundy: #6e141c;
    --burgundy-deep: #5e1118;
    --gold: #c98a3a;
    --gold-light: #d69a45;
    --brown: #9a5a2a;
    --ink: #111111;
    --text-light: #ffffff;
  }
  html, body {
    margin: 0;
    width: 900px;
    height: 1200px;
    overflow: hidden;
  }
  body {
    background: radial-gradient(ellipse at 50% 30%, var(--stage-top), var(--stage-bottom) 75%);
    font-family: "Lato", Arial, sans-serif;
  }
  .card {
    position: absolute;
    left: 128px;
    width: 647px;
    height: 377px;
    border-radius: 28px;
    overflow: hidden;
    box-shadow: 0 6px 18px rgba(0,0,0,0.6);
  }
  .card-front { top: 101px; }
  .card-back { top: 575px; height: 375px; }
  .card svg.shape { position: absolute; inset: 0; }
  .brand {
    position: absolute;
    display: flex;
    flex-direction: column;
    align-items: center;
  }
  .brand-square {
    background: var(--burgundy);
  }
  .brand-name {
    font-weight: 700;
    color: var(--ink);
    letter-spacing: 0.5px;
    line-height: 1;
  }
  .front-brand { left: 83px; top: 75px; width: 183px; }
  .front-brand .brand-square { width: 183px; height: 183px; }
  .front-brand .brand-name { font-size: 27px; margin-top: 10px; }
  .back-brand { left: 244px; top: 77px; width: 161px; }
  .back-brand .brand-square { width: 161px; height: 161px; }
  .back-brand .brand-name { font-size: 24px; margin-top: 9px; }
  .contact {
    position: absolute;
    left: 378px;
    top: 126px;
    color: var(--text-light);
  }
  .contact-name { font-size: 22px; margin: 0; font-weight: 400; letter-spacing: 0.3px; }
  .contact-title { font-size: 16px; color: var(--gold-light); margin: 1px 0 14px; }
  .contact-line {
    display: flex;
    align-items: center;
    gap: 6px;
    font-size: 16px;
    height: 23px;
  }
  .contact-line svg { width: 15px; height: 13px; fill: var(--text-light); }
  .back-url {
    position: absolute;
    left: 0; right: 0;
    top: 344px;
    text-align: center;
    color: var(--text-light);
    font-size: 18px;
    letter-spacing: 0.2px;
  }
</style>
</head>
<body>

<section class="card card-front">
  <svg class="shape" width="647" height="377" viewBox="0 0 647 377">
    <defs>
      <linearGradient id="frontBand" x1="0" x2="1" y1="0" y2="0">
        <stop offset="0" stop-color="#6e141c"/>
        <stop offset="0.72" stop-color="#6e141c"/>
        <stop offset="1" stop-color="#b87a35"/>
      </linearGradient>
      <linearGradient id="sideTab" x1="0" x2="0" y1="0" y2="1">
        <stop offset="0" stop-color="#8a3a20"/>
        <stop offset="1" stop-color="#a0602a"/>
      </linearGradient>
    </defs>
    <rect width="647" height="377" fill="url(#frontBand)"/>
    <rect width="30" height="377" fill="url(#sideTab)"/>
    <polygon fill="#ffffff"
      points="0,0 321,0 321,82 347,104 347,274 321,297 321,377 0,377 0,297 22,277 22,104 0,84"/>
  </svg>

  <div class="brand front-brand">
    <div class="brand-square"></div>
    <div class="brand-name">BROVENNA</div>
  </div>

  <div class="contact">
    <h1 class="contact-name">Marcus T. Hollenbrand</h1>
    <p class="contact-title">CEO</p>
    <div class="contact-line">
      <svg viewBox="0 0 16 14"><path d="M1 5 C1 1 15 1 15 5 L12 6 L11 4 L5 4 L4 6 Z M4 7 L12 7 L14 13 L2 13 Z"/></svg>
      <span>555-294-6172</span>
    </div>
    <div class="contact-line">
      <svg viewBox="0 0 16 14"><path d="M1 2 H15 V12 H1 Z M2 3 L8 8 L14 3 Z" fill-rule="evenodd"/></svg>
      <span>mark@brovennatrading.example</span>
    </div>
    <div class="contact-line">
      <svg viewBox="0 0 16 14"><path d="M1 1 H15 V10 H1 Z M2.5 2.5 V8.5 H13.5 V2.5 Z M6 11 H10 V12 H12 V13 H4 V12 H6 Z" fill-rule="evenodd"/></svg>
      <span>www.brovennatrading.example</span>
    </div>
  </div>
</section>

<section class="card card-back">
  <svg class="shape" width="647" height="375" viewBox="0 0 647 375">
    <defs>
      <linearGradient id="bottomBand" x1="0" x2="0" y1="0" y2="1">
        <stop offset="0" stop-color="#d08e3c"/>
        <stop offset="1" stop-color="#96502a"/>
      </linearGradient>
      <linearGradient id="topTab" x1="0" x2="0" y1="0" y2="1">
        <stop offset="0" stop-color="#d49441"/>
        <stop offset="1" stop-color="#b8762f"/>
      </linearGradient>
    </defs>
    <rect width="647" height="375" fill="#ffffff"/>
    <polygon fill="url(#topTab)" points="182,0 465,0 437,31 212,31"/>
    <polygon fill="url(#bottomBand)" points="0,305 182,305 212,335 437,335 465,305 647,305 647,375 0,375"/>
  </svg>

  <div class="brand back-brand">
    <div class="brand-square"></div>
    <div class="brand-name">BROVENNA</div>
  </div>

  <div class="back-url">www.brovennatrading.example</div>
</section>

</body>
</html>
```